We need a poster design for "KORVEN Sports Night" events. The events have been around for 3 years and we hope the poster will give a sense of vibrant and active designs. It is more to a community event with teamwork and fun.

I have uploaded a past event poster just FYI.

Target Market(s)

Community, Family

Industry/Entity Type

Non Profit

Logo Text

KORVEN Sports Night

Requirements
Must have
• KORVEN Sports Night
• Organiser: KORVEN Sydney
• Date: 25/11/2017
• Time: 4:00pm
• Venue: Wendilow Park
• Facebook: korvenplay

```html
<!DOCTYPE html>
<html lang="en">
<head>
<meta charset="utf-8">
<title>KORVEN Sports Night</title>
<link rel="stylesheet" href="https://fonts.googleapis.com/css2?family=Archivo+Black&family=Roboto+Condensed:wght@700&display=swap">
<style>
  :root {
    --brand-red: #a8101c;
    --title-shadow: #d4d4d4;
    --paper: #f7f7f7;
    --mist: #e4e4e4;
    --track-pale: #c9d7ec;
    --track-light: #8fb0dc;
    --track-blue: #3f6db3;
    --track-deep: #27499a;
    --runner-red: #e6283f;
    --runner-coral: #f26a4f;
    --runner-yellow: #f7d23c;
    --runner-amber: #f5a623;
    --runner-purple: #8a3fa8;
    --runner-violet: #5a4fb0;
  }
  * { margin: 0; padding: 0; box-sizing: border-box; }
  html, body { width: 858px; height: 1200px; overflow: hidden; background: var(--paper); }
  .poster {
    position: relative;
    width: 858px;
    height: 1200px;
    overflow: hidden;
    background: var(--paper);
  }
  .poster__artwork {
    position: absolute;
    inset: 0;
    background:
      radial-gradient(ellipse 250px 500px at 650px 760px, var(--runner-red) 0%, var(--runner-coral) 40%, rgba(242, 106, 79, 0.6) 62%, transparent 82%),
      radial-gradient(ellipse 135px 380px at 360px 640px, var(--runner-yellow) 0%, var(--runner-amber) 45%, rgba(245, 166, 35, 0.5) 65%, transparent 85%),
      radial-gradient(ellipse 120px 330px at 130px 560px, var(--runner-purple) 0%, var(--runner-violet) 50%, rgba(90, 79, 176, 0.5) 68%, transparent 88%),
      linear-gradient(168deg, var(--paper) 0%, var(--mist) 26%, var(--track-pale) 44%, var(--track-light) 58%, var(--track-blue) 78%, var(--track-deep) 100%);
  }
  .poster__title {
    position: absolute;
    left: 0;
    top: 0;
    width: 858px;
    height: 280px;
  }
  .title-main, .title-sub {
    font-family: "Archivo Black", "Arial Black", sans-serif;
  }
  .title-main { font-size: 180px; }
  .title-sub { font-size: 82px; }
  .title-fill { fill: var(--brand-red); }
  .title-shadow { fill: var(--title-shadow); }
  .event-details {
    position: absolute;
    left: 32px;
    top: 874px;
    list-style: none;
    font-family: "Roboto Condensed", "Arial Narrow", sans-serif;
    font-weight: 700;
    font-size: 41px;
    line-height: 49px;
    color: var(--brand-red);
  }
  .event-details__social {
    display: flex;
    align-items: center;
    gap: 12px;
  }
  .social-square {
    width: 28px;
    height: 28px;
    background: var(--track-deep);
  }
</style>
</head>
<body>
  <main class="poster">
    <div class="poster__artwork" role="img" aria-label="Three runners in faceted purple, yellow and red tones jogging away across a blue patterned track on a pale splattered background"></div>

    <svg class="poster__title" viewBox="0 0 858 280" aria-label="KORVEN Sports Night">
      <text class="title-main title-shadow" x="77" y="184" textLength="712" lengthAdjust="spacingAndGlyphs">KORVEN</text>
      <text class="title-main title-fill" x="71" y="178" textLength="712" lengthAdjust="spacingAndGlyphs">KORVEN</text>
      <text class="title-sub title-shadow" x="74" y="252" textLength="719" lengthAdjust="spacingAndGlyphs">Sports Night</text>
      <text class="title-sub title-fill" x="69" y="247" textLength="719" lengthAdjust="spacingAndGlyphs">Sports Night</text>
    </svg>

    <ul class="event-details">
      <li>KORVEN Sports Night</li>
      <li>Organiser: KORVEN Sydney</li>
      <li>Date: 25/11/2017</li>
      <li>Time: 4:00pm</li>
      <li>Venue: Wendilow Park</li>
      <li class="event-details__social"><span class="social-square"></span>korvenplay</li>
    </ul>
  </main>
</body>
</html>
```